Amber Reed Landing Postcard Design

I am a real estate agent
I am marketing a gulf access waterfront community is southwest florida. I would like to do Just Listed and Just Sold post cards

So this will be two different post cards

In addition to the pictures I have uploaded mock ups of an idea of what I would like for the front and the back

I would like this done glossy on both sides

```html
<!DOCTYPE html>
<html lang="en">
<head>
<meta charset="utf-8">
<title>Amber Reed Landing – Just Sold Postcard</title>
<link href="https://fonts.googleapis.com/css2?family=Cinzel:wght@400;600&family=Cormorant+Garamond:ital,wght@1,500&family=Marcellus&family=PT+Sans&display=swap" rel="stylesheet">
<style>
  :root {
    --sand: #c9b99b;
    --gulf-blue: #1f78c1;
    --ink: #1b1b1b;
    --paper: #ffffff;
    --photo-blue: #4a79b8;
    --photo-blue-deep: #3a5f7c;
    --thumb-tone: #6f8fa8;
    --map-tone: #8fbf8f;
    --beach-light: #dcdcdc;
    --beach-mid: #bdbdbd;
    --rule: #333333;
  }
  * { margin: 0; padding: 0; box-sizing: border-box; }
  html, body { width: 925px; height: 1200px; overflow: hidden; background: var(--paper); }
  .canvas { position: relative; width: 925px; height: 1200px; font-family: "Cinzel", serif; color: var(--ink); }

  /* Front of card */
  .front-sand { position: absolute; left: 60px; top: 0; width: 302px; height: 502px; background: var(--sand); }
  .community-label { position: absolute; left: 108px; top: 14px; font-family: "PT Sans", sans-serif; font-size: 22px; color: #2b2b2b; }
  .front-title {
    position: absolute; left: 10px; top: 46px; writing-mode: vertical-rl;
    font-family: "Cormorant Garamond", serif; font-style: italic; font-weight: 500;
    font-size: 80px; line-height: 1; color: var(--ink);
  }
  .hero-photo {
    position: absolute; left: 109px; top: 45px; width: 751px; height: 432px;
    background: linear-gradient(180deg, var(--photo-blue) 0%, var(--photo-blue-deep) 100%);
    box-shadow: 6px 8px 10px rgba(0,0,0,0.45);
  }
  .thumb {
    position: absolute; left: 708px; width: 126px; height: 124px;
    border: 4px solid var(--paper); border-radius: 12px;
    background: var(--thumb-tone);
    box-shadow: 2px 3px 6px rgba(0,0,0,0.4);
  }
  .thumb--aerial { top: 60px; }
  .thumb--map { top: 201px; background: var(--map-tone); border-color: #1f6fb5; }
  .thumb--coast { top: 340px; }

  .front-band { position: absolute; left: 60px; top: 502px; width: 865px; height: 100px; background: var(--gulf-blue); }
  .brand-mark { position: absolute; display: flex; align-items: center; gap: 5px; }
  .brand-mark__square { width: 18px; height: 18px; background: currentColor; flex: none; }
  .brand-mark__name { font-family: "Cinzel", serif; font-size: 8px; line-height: 10px; width: 44px; }
  .front-band .brand-mark { left: 30px; top: 32px; color: var(--paper); }
  .front-contact { position: absolute; left: 164px; top: 518px; font-size: 13px; line-height: 15px; color: var(--paper); }

  .card-divider { position: absolute; left: 0; top: 628px; width: 925px; height: 1.5px; background: var(--rule); }

  /* Back of card */
  .back-photo {
    position: absolute; left: 52px; top: 655px; width: 567px; height: 485px;
    background: linear-gradient(180deg, var(--beach-mid) 0%, var(--beach-light) 100%);
  }
  .back-photo .brand-mark { left: 46px; top: 18px; color: var(--ink); flex-direction: column; align-items: flex-start; gap: 6px; }
  .back-photo .brand-mark__square { width: 30px; height: 30px; }
  .back-photo .brand-mark__name { font-size: 11px; line-height: 13px; width: 70px; }
  .back-contact { position: absolute; left: 208px; top: 668px; font-size: 20px; line-height: 25px; }
  .back-title {
    position: absolute; left: 160px; top: 760px;
    font-family: "Cormorant Garamond", serif; font-style: italic; font-weight: 500; font-size: 76px;
  }
  .title-rule { position: absolute; left: 62px; top: 890px; width: 470px; height: 2px; background: var(--rule); }
  .sold-location { position: absolute; left: 62px; top: 903px; width: 470px; text-align: center; font-size: 25px; font-weight: 600; }
  .sale-details { position: absolute; left: 58px; top: 972px; font-size: 15px; }
  .fill-line { display: inline-block; border-bottom: 1px solid var(--ink); vertical-align: baseline; }
  .fill-line--price { width: 190px; margin-right: 24px; }
  .fill-line--date { width: 200px; margin-left: 8px; }
  .invite { position: absolute; left: 52px; top: 1010px; width: 567px; text-align: center; font-size: 17px; line-height: 22px; }
  .phone { position: absolute; left: 52px; top: 1058px; width: 567px; text-align: center; font-family: "Marcellus", serif; font-size: 38px; }
  .email { position: absolute; left: 52px; top: 1108px; width: 567px; text-align: center; font-size: 17px; }

  .badge { position: absolute; top: 1148px; border: 2px solid var(--ink); }
  .badge--housing { left: 52px; width: 44px; height: 42px; }
  .badge--listing { left: 107px; width: 56px; height: 38px; top: 1150px; }
</style>
</head>
<body>
<div class="canvas">
  <!-- Front -->
  <div class="front-sand"></div>
  <div class="community-label">Amber Reed Landing</div>
  <div class="front-title">Just Sold</div>
  <div class="hero-photo" role="img" aria-label="Photo of a waterfront canal with homes and a boat"></div>
  <div class="thumb thumb--aerial" role="img" aria-label="Aerial photo of the community"></div>
  <div class="thumb thumb--map" role="img" aria-label="Map showing the community location in Florida"></div>
  <div class="thumb thumb--coast" role="img" aria-label="Aerial photo of the gulf coast"></div>

  <div class="front-band">
    <div class="brand-mark"><span class="brand-mark__square"></span><span class="brand-mark__name">Harbor Reach</span></div>
  </div>
  <div class="front-contact">CLARA WHITFIELD<br>Harbor Reach Realty<br>PO Box 418<br>Palm Inlet, FL 33900</div>

  <div class="card-divider"></div>

  <!-- Back -->
  <div class="back-photo" role="img" aria-label="Black and white photo of a beach with footprints">
    <div class="brand-mark"><span class="brand-mark__square"></span><span class="brand-mark__name">Harbor Reach</span></div>
  </div>
  <div class="back-contact">CLARA WHITFIELD<br>Harbor Reach Realty<br>PO Box 418<br>Palm Inlet, FL 33900</div>
  <div class="back-title">Just Sold</div>
  <div class="title-rule"></div>
  <div class="sold-location">In Amber Reed Landing</div>
  <div class="sale-details">at $<span class="fill-line fill-line--price"></span>On<span class="fill-line fill-line--date"></span></div>
  <div class="invite">Please contact me if you are interested<br>in buying or selling property in the area.</div>
  <div class="phone">555-318-2047</div>
  <div class="email">clarawhitfield@example.com</div>

  <div class="badge badge--housing"></div>
  <div class="badge badge--listing"></div>
</div>
</body>
</html>
```